Brindlewort Organic

Please find attached screenshots of a same product as what I'm selling, looking for similar packaging but yet a whole new different design with my own logo plumtiles which is also attached. It will be on white bags with the clear on the bottom center. As far as colors maby green yellow and black or if you have a better idea. Also it needs to be something that looks up to date modern I like when it has that two-tone gloss to it where it goes from darker to lighter.

```html
<!DOCTYPE html>
<html lang="en">
<head>
<meta charset="utf-8">
<title>Brindlewort Organic – Herbs for Wellness Pouch</title>
<link rel="stylesheet" href="https://fonts.googleapis.com/css2?family=Oswald:wght@500;700&family=Courgette&display=swap">
<style>
  :root {
    --backdrop: #6b6b6b;
    --bag-white: #f5f5f3;
    --ink-black: #141414;
    --green-deep: #145c2e;
    --green-bright: #3fa34d;
    --lime: #8cc63f;
    --sun-yellow: #f5c518;
    --text-white: #ffffff;
    --herb-dark: #5d6b2e;
    --herb-light: #9aa85a;
  }
  html, body {
    margin: 0;
    padding: 0;
    width: 1200px;
    height: 1118px;
    overflow: hidden;
    background: var(--backdrop);
  }
  .canvas {
    position: relative;
    width: 1200px;
    height: 1118px;
  }
  .pouch {
    position: absolute;
    inset: 0;
    width: 1200px;
    height: 1118px;
  }
  .tagline {
    font-family: "Oswald", sans-serif;
    font-weight: 700;
    font-size: 28px;
    letter-spacing: 6px;
    fill: var(--text-white);
  }
  .product-name {
    font-family: "Courgette", cursive;
    font-size: 72px;
    fill: var(--sun-yellow);
  }
  .product-sub {
    font-family: "Oswald", sans-serif;
    font-weight: 500;
    font-size: 26px;
    letter-spacing: 12px;
    fill: var(--text-white);
  }
  .brand-name {
    font-family: "Oswald", sans-serif;
    font-weight: 500;
    font-size: 32px;
    letter-spacing: 2px;
    fill: var(--ink-black);
  }
  .net-weight {
    font-family: "Oswald", sans-serif;
    font-weight: 500;
    font-size: 20px;
    letter-spacing: 1px;
    fill: var(--text-white);
  }
</style>
</head>
<body>
<main class="canvas">
  <svg class="pouch" viewBox="0 0 1200 1118" xmlns="http://www.w3.org/2000/svg">
    <defs>
      <linearGradient id="gloss-band" x1="0" y1="0" x2="1" y2="1">
        <stop offset="0%" stop-color="var(--ink-black)"/>
        <stop offset="45%" stop-color="var(--green-deep)"/>
        <stop offset="80%" stop-color="var(--green-bright)"/>
        <stop offset="100%" stop-color="var(--lime)"/>
      </linearGradient>
      <linearGradient id="gloss-sheen" x1="0" y1="0" x2="0" y2="1">
        <stop offset="0%" stop-color="#ffffff" stop-opacity="0.22"/>
        <stop offset="50%" stop-color="#ffffff" stop-opacity="0"/>
      </linearGradient>
      <linearGradient id="base-band" x1="0" y1="0" x2="1" y2="0">
        <stop offset="0%" stop-color="var(--ink-black)"/>
        <stop offset="100%" stop-color="var(--green-deep)"/>
      </linearGradient>
      <linearGradient id="window-fill" x1="0" y1="0" x2="0" y2="1">
        <stop offset="0%" stop-color="var(--herb-light)"/>
        <stop offset="100%" stop-color="var(--herb-dark)"/>
      </linearGradient>
      <clipPath id="pouch-clip">
        <rect x="320" y="90" width="560" height="950" rx="20"/>
      </clipPath>
    </defs>

    <!-- bag body -->
    <rect class="bag-body" x="320" y="90" width="560" height="950" rx="20" fill="var(--bag-white)"/>

    <g clip-path="url(#pouch-clip)">
      <!-- zipper seal -->
      <line x1="346" y1="196" x2="854" y2="196" stroke="#dcdcdc" stroke-width="3"/>
      <line x1="346" y1="208" x2="854" y2="208" stroke="#dcdcdc" stroke-width="2"/>

      <!-- two-tone gloss band -->
      <path class="gloss-band" d="M320 270 L880 240 V500 L320 540 Z" fill="url(#gloss-band)"/>
      <path class="gloss-sheen" d="M320 270 L880 240 V380 L320 410 Z" fill="url(#gloss-sheen)"/>

      <!-- yellow accent stripe -->
      <path class="accent-stripe" d="M320 540 L880 500 V514 L320 554 Z" fill="var(--sun-yellow)"/>

      <!-- base band -->
      <rect class="base-band" x="320" y="965" width="560" height="75" fill="url(#base-band)"/>
    </g>

    <!-- organic seal (plain shape) -->
    <circle class="organic-seal" cx="808" cy="152" r="34" fill="var(--sun-yellow)"/>

    <!-- band type -->
    <text class="tagline" x="600" y="328" text-anchor="middle">HERBS FOR WELLNESS</text>
    <text class="product-name" x="600" y="420" text-anchor="middle">Brindlewort</text>
    <text class="product-sub" x="606" y="468" text-anchor="middle">ORGANIC</text>

    <!-- brand -->
    <circle class="brand-dot" cx="534" cy="616" r="12" fill="var(--green-deep)"/>
    <text class="brand-name" x="556" y="628">plumtiles</text>

    <!-- clear window -->
    <g role="img" aria-label="Clear window showing the dried brindlewort leaves inside">
      <rect x="470" y="690" width="260" height="240" rx="40" fill="url(#window-fill)"/>
    </g>
    <rect class="window-frame" x="470" y="690" width="260" height="240" rx="40" fill="none" stroke="var(--ink-black)" stroke-width="4"/>
    <path class="window-shine" d="M498 720 Q520 702 560 700" fill="none" stroke="#ffffff" stroke-opacity="0.6" stroke-width="6" stroke-linecap="round"/>

    <!-- net weight -->
    <text class="net-weight" x="600" y="1010" text-anchor="middle">NET WT. 1.27 OZ. (36g)</text>
  </svg>
</main>
</body>
</html>
```